An our door sign really promoting our clinic and services

We have a new sports medicine clinic called ASHBRAE SPORTS MEDICINE.
We want to make a really nice external sign at our clinic using a photo of our team we really like. I have attached the photo.
We want to simply include our LOGO and also signs with these slogan options. So we want different signs with these different slogans so we can choose what we really like.
This should be a simple and quite design.

The SLOGANS WE WOULD LIKE TO SEE ON THE SIGN (only one slogan per sign in the drafts)

1. Your Journey. Our Expertise
2. Where better health begins
3. Building the best version of you
4. Your health, in expert hands
5. Reaching new heights in your health
6. Your path to peak performance starts here

I have also included different versions of our logo based on the background and how you set the sign up

So summary
1. Image attached
2. Slogan options we would like to see them all
3. Logo attached (various options based on how you set the background up)
4. Size of sign is 2935mm wide x 1885mm high

```html
<!DOCTYPE html>
<html lang="en">
<head>
<meta charset="utf-8">
<title>Ashbrae Sports Medicine – Exterior Sign Drafts</title>
<link href="https://fonts.googleapis.com/css2?family=Saira+Extra+Condensed:ital,wght@0,800;1,900&display=swap" rel="stylesheet">
<style>
  :root {
    --page-grey: #b3b3b3;
    --navy: #18184a;
    --cyan: #4cc6ea;
    --sky: #2aa4dd;
    --white: #ffffff;
  }
  * { margin: 0; padding: 0; box-sizing: border-box; }
  html, body { width: 1200px; height: 2700px; overflow: hidden; }
  body {
    background: var(--page-grey);
    position: relative;
    font-family: "Saira Extra Condensed", "Arial Narrow", sans-serif;
  }
  .sign {
    position: absolute;
    left: 117px;
    width: 965px;
    height: 620px;
    background: var(--navy);
    overflow: hidden;
    box-shadow: 0 2px 6px rgba(0,0,0,0.25);
  }
  .sign--journey { top: 205px; }
  .sign--heights { top: 1040px; }
  .sign--path { top: 1893px; }

  .sign__art { position: absolute; inset: 0; width: 965px; height: 620px; }

  .brand {
    position: absolute;
    top: 122px;
    left: 70px;
    display: flex;
    align-items: center;
    gap: 16px;
    white-space: nowrap;
  }
  .sign--path .brand { left: 92px; }
  .brand__dot {
    width: 22px; height: 22px;
    border-radius: 50%;
    background: var(--cyan);
    flex: none;
  }
  .brand__name {
    color: var(--white);
    font-weight: 800;
    font-size: 38px;
    line-height: 0.95;
    letter-spacing: 3px;
  }

  .slogan-text {
    font-family: "Saira Extra Condensed", "Arial Narrow", sans-serif;
    font-style: italic;
    font-weight: 900;
    text-transform: uppercase;
  }
  .slogan-text--white { fill: var(--white); }
  .slogan-text--cyan { fill: var(--cyan); }
</style>
</head>
<body>

<section class="sign sign--journey">
  <svg class="sign__art" viewBox="0 0 965 620">
    <defs>
      <linearGradient id="bandA" x1="0" y1="0" x2="0" y2="1">
        <stop offset="0" stop-color="#1f3f86"/><stop offset="0.5" stop-color="#2b6aa8"/><stop offset="1" stop-color="#4cc6ea"/>
      </linearGradient>
      <linearGradient id="photoA" x1="0" y1="0" x2="1" y2="1">
        <stop offset="0" stop-color="#c9ccd0"/><stop offset="0.5" stop-color="#5b5e66"/><stop offset="1" stop-color="#2c3a2e"/>
      </linearGradient>
      <linearGradient id="ribbonA" x1="0" y1="0" x2="1" y2="0">
        <stop offset="0" stop-color="#4cc6ea"/><stop offset="0.62" stop-color="#4cc6ea"/><stop offset="1" stop-color="#4cc6ea" stop-opacity="0"/>
      </linearGradient>
    </defs>
    <path d="M575 0 C500 200 500 450 620 620 L965 620 L965 0 Z" fill="url(#bandA)"/>
    <path d="M698 0 C560 160 520 340 600 480 C630 540 660 590 690 620 L965 620 L965 0 Z" fill="var(--sky)"/>
    <path d="M818 0 C660 170 560 330 635 480 C665 540 700 590 728 620 L965 620 L965 0 Z" fill="url(#photoA)" role="img" aria-label="Team photo: clinician with tablet talking with an athlete in the gym"/>

    <rect class="banner" x="0" y="393" width="505" height="94" fill="url(#ribbonA)"/>
    <text class="slogan-text slogan-text--white" x="53" y="370" font-size="112" textLength="402" lengthAdjust="spacingAndGlyphs">YOUR <tspan class="slogan-text--cyan">HEALTH</tspan></text>
    <text class="slogan-text slogan-text--white" x="25" y="475" font-size="94" textLength="433" lengthAdjust="spacingAndGlyphs">IN EXPERT HANDS</text>
  </svg>
  <div class="brand"><span class="brand__dot"></span><span class="brand__name">ASHBRAE<br>SPORTS MEDICINE</span></div>
</section>

<section class="sign sign--heights">
  <svg class="sign__art" viewBox="0 0 965 620">
    <defs>
      <linearGradient id="bandB" x1="0" y1="0" x2="0" y2="1">
        <stop offset="0" stop-color="#1f3f86"/><stop offset="0.5" stop-color="#2b6aa8"/><stop offset="1" stop-color="#4cc6ea"/>
      </linearGradient>
      <linearGradient id="photoB" x1="0" y1="0" x2="1" y2="1">
        <stop offset="0" stop-color="#c9ccd0"/><stop offset="0.5" stop-color="#5b5e66"/><stop offset="1" stop-color="#2c3a2e"/>
      </linearGradient>
      <linearGradient id="ribbonB" x1="0" y1="0" x2="1" y2="0">
        <stop offset="0" stop-color="#4cc6ea"/><stop offset="0.62" stop-color="#4cc6ea"/><stop offset="1" stop-color="#4cc6ea" stop-opacity="0"/>
      </linearGradient>
    </defs>
    <path d="M575 0 C500 200 500 450 620 620 L965 620 L965 0 Z" fill="url(#bandB)"/>
    <path d="M698 0 C560 160 520 340 600 480 C630 540 660 590 690 620 L965 620 L965 0 Z" fill="var(--sky)"/>
    <path d="M818 0 C660 170 560 330 635 480 C665 540 700 590 728 620 L965 620 L965 0 Z" fill="url(#photoB)" role="img" aria-label="Team photo: clinician with tablet talking with an athlete in the gym"/>

    <rect class="banner" x="0" y="422" width="505" height="95" fill="url(#ribbonB)"/>
    <text class="slogan-text slogan-text--white" x="66" y="330" font-size="88" textLength="370" lengthAdjust="spacingAndGlyphs">REACHING NEW</text>
    <text class="slogan-text slogan-text--cyan" x="121" y="410" font-size="96" textLength="240" lengthAdjust="spacingAndGlyphs">HEIGHTS</text>
    <text class="slogan-text slogan-text--white" x="28" y="505" font-size="96" textLength="425" lengthAdjust="spacingAndGlyphs">IN YOUR HEALTH</text>
  </svg>
  <div class="brand"><span class="brand__dot"></span><span class="brand__name">ASHBRAE<br>SPORTS MEDICINE</span></div>
</section>

<section class="sign sign--path">
  <svg class="sign__art" viewBox="0 0 965 620">
    <defs>
      <linearGradient id="bandC" x1="0" y1="0" x2="0" y2="1">
        <stop offset="0" stop-color="#1f3f86"/><stop offset="0.5" stop-color="#2b6aa8"/><stop offset="1" stop-color="#4cc6ea"/>
      </linearGradient>
      <linearGradient id="photoC" x1="0" y1="0" x2="1" y2="1">
        <stop offset="0" stop-color="#c9ccd0"/><stop offset="0.5" stop-color="#5b5e66"/><stop offset="1" stop-color="#2c3a2e"/>
      </linearGradient>
      <linearGradient id="ribbonC" x1="0" y1="0" x2="1" y2="0">
        <stop offset="0" stop-color="#4cc6ea"/><stop offset="0.62" stop-color="#4cc6ea"/><stop offset="1" stop-color="#4cc6ea" stop-opacity="0"/>
      </linearGradient>
    </defs>
    <path d="M597 0 C522 200 522 450 642 620 L965 620 L965 0 Z" fill="url(#bandC)"/>
    <path d="M720 0 C582 160 542 340 622 480 C652 540 682 590 712 620 L965 620 L965 0 Z" fill="var(--sky)"/>
    <path d="M840 0 C682 170 582 330 657 480 C687 540 722 590 750 620 L965 620 L965 0 Z" fill="url(#photoC)" role="img" aria-label="Team photo: clinician with tablet talking with an athlete in the gym"/>

    <rect class="banner" x="0" y="425" width="525" height="92" fill="url(#ribbonC)"/>
    <text class="slogan-text slogan-text--white" x="111" y="342" font-size="76" textLength="292" lengthAdjust="spacingAndGlyphs">YOUR PATH TO</text>
    <text class="slogan-text slogan-text--cyan" x="31" y="417" font-size="82" textLength="457" lengthAdjust="spacingAndGlyphs">PEAK PERFORMANCE</text>
    <text class="slogan-text slogan-text--white" x="58" y="507" font-size="104" textLength="370" lengthAdjust="spacingAndGlyphs">STARTS HERE</text>
  </svg>
  <div class="brand"><span class="brand__dot"></span><span class="brand__name">ASHBRAE<br>SPORTS MEDICINE</span></div>
</section>

</body>
</html>
```